Newsletter (nur grafisch) Kreditvermittlung Alu-Kasse
Kreditsuchende stellen bei uns EINEN Kreditantrag und wir verhandeln mit bis zu 20 Banken und präsentieren dem Kunden dann das beste Angebot absolut kostenlos und unverbindlich.
Spezielle Landingpage:
www.alu-kasse-muster.de/kredit.htm
Wir wollen eine Newslettervorlage, die dieses Angebot bewirbt. Wir brauchen nur das Design - die Umsetzung in html können wir dann selbst.
Die notwendigen Bilddateien müssen vom Gewinner zur Verfügung gestellt werden.
Skizzenhafte Ausführung bei Dingen, die klar sind (z.B. Header) genügen.
Text kann Fülltext verwendet werden oder Sie schreiben schnell eine Kleinigkeit, inspiriert durch die Landingpage.
Wir sind mittlerweile betriebsblind und für jeden frischen Wind dankbar!
Langfristige Zusammenarbeit:
Wir benötigen ständig Grafiken, Werbemittel und html-Arbeiten. Der Gewinner dieses Wettbewerbs kann sich auf weitere lukrative Aufträge freuen!

```html
<!DOCTYPE html>
<html lang="de">
<head>
<meta charset="utf-8">
<title>Alu-Kasse Newsletter April 2011</title>
<link rel="stylesheet" href="https://fonts.googleapis.com/css2?family=Arimo:wght@400;700&display=swap">
<style>
  :root {
    --teal-dark: #114a55;
    --teal-band: #5f8790;
    --panel: #b9d3d8;
    --header-strip: #d9e3e5;
    --card: #ffffff;
    --divider: #a9cbc9;
    --text: #1c1c1c;
    --red: #d5202b;
    --red-dark: #a3111b;
    --beige: #cdc6b4;
    --white: #ffffff;
    --font: "Arimo", Arial, Helvetica, sans-serif;
  }
  html, body { margin: 0; padding: 0; }
  body {
    width: 1200px; height: 1200px; overflow: hidden;
    background: var(--white); font-family: var(--font); color: var(--text);
    position: relative;
  }
  .abs { position: absolute; }

  .header-visual {
    left: 380px; top: 0; width: 820px; height: 144px;
    background: linear-gradient(90deg, #ffffff 0%, #e9e6ee 30%, #d8cfe0 60%, #cfd8c8 100%);
  }
  .header-strip { left: 0; top: 144px; width: 1200px; height: 36px; background: var(--header-strip); }
  .header-square { left: 864px; top: 144px; width: 56px; height: 36px; background: var(--beige); }
  .issue-tag {
    left: 944px; top: 144px; width: 256px; height: 36px; background: var(--teal-band);
    color: var(--white); font-size: 17px; line-height: 36px; padding-left: 16px; box-sizing: border-box;
  }
  .brand-name {
    left: 118px; top: 100px; font-size: 96px; font-weight: 400; color: var(--teal-dark);
    line-height: 1; letter-spacing: 1px;
  }
  .top-bar {
    left: 0; top: 192px; width: 1200px; height: 40px; background: var(--teal-dark); color: var(--white);
  }
  .top-bar .tagline { position: absolute; left: 456px; top: 0; line-height: 40px; font-size: 21px; font-weight: 700; letter-spacing: 0.5px; }
  .top-bar .web { position: absolute; left: 960px; top: 0; line-height: 40px; font-size: 17px; }

  .panel { left: 64px; top: 232px; width: 1072px; height: 900px; background: var(--panel); }

  .offer-card {
    left: 104px; top: 280px; width: 760px; height: 770px; background: var(--card); border-radius: 14px;
  }
  .offer-title { position: absolute; left: 26px; top: 34px; margin: 0; font-size: 26px; font-weight: 700; }
  .offer-list {
    position: absolute; left: 26px; top: 96px; width: 700px; margin: 0; padding: 0; list-style: none;
    font-size: 22px; line-height: 33px;
  }
  .offer-list li { padding-left: 16px; text-indent: -16px; margin-bottom: 6px; }
  .card-divider { position: absolute; left: 0; top: 494px; width: 760px; height: 2px; background: var(--divider); }

  .cta-button {
    position: absolute; left: 40px; top: 526px; width: 228px; height: 210px; border-radius: 16px;
    background: linear-gradient(180deg, #e8323c 0%, var(--red) 50%, var(--red-dark) 100%);
    box-shadow: 2px 3px 6px rgba(0,0,0,0.35);
    color: var(--white); text-align: center; font-weight: 700; display: flex; flex-direction: column;
    justify-content: center; font-size: 23px; line-height: 34px;
  }
  .cta-button .big { font-size: 34px; line-height: 44px; }
  .guarantee { position: absolute; left: 300px; top: 572px; width: 440px; }
  .guarantee h2 { margin: 0 0 8px; font-size: 26px; font-weight: 700; }
  .guarantee p { margin: 0; font-size: 21px; line-height: 30px; }

  .starburst { left: 850px; top: 280px; width: 300px; height: 300px; }
  .starburst-text {
    left: 850px; top: 280px; width: 300px; height: 300px; display: flex; align-items: center; justify-content: center;
    text-align: center; color: var(--white); font-weight: 700; font-size: 23px; line-height: 28px;
    transform: rotate(-14deg);
  }

  .quality-badge { left: 916px; top: 816px; width: 164px; height: 196px; background: linear-gradient(180deg,#f2f4f4,#c9d1d3); border: 2px solid #9aa8ab; box-sizing: border-box; }
  .security-seal { left: 922px; top: 1028px; width: 148px; height: 148px; border-radius: 50%; background: #e8b62a; border: 8px solid #1f4e8a; box-sizing: border-box; }

  .footer-bar {
    left: 0; top: 1132px; width: 1200px; height: 44px; background: var(--teal-dark); color: #f3e6c8;
    font-size: 17px; line-height: 44px;
  }
  .footer-bar .links { position: absolute; left: 160px; }
</style>
</head>
<body>
  <div class="abs header-visual" role="img" aria-label="Fliegende Euro-Geldscheine"></div>
  <div class="abs header-strip"></div>
  <div class="abs header-square"></div>
  <div class="abs issue-tag">Newsletter April 2011</div>
  <div class="abs brand-name">Alu-Kasse</div>

  <div class="abs top-bar">
    <span class="tagline">KREDIT - seit 35 Jahren</span>
    <span class="web">www.alu-kasse-muster.de</span>
  </div>

  <div class="abs panel"></div>

  <section class="abs offer-card">
    <h1 class="offer-title">Kredite als Sofortkredit (auch ohne Bonitek)!</h1>
    <ul class="offer-list">
      <li>- Sofortkredit bis 100.000,- Euro</li>
      <li>- Nebenkredit bis 50.000,- Euro (günstige Darlehen)</li>
      <li>- Kredit zur freien Verwendung (z.B. Umschuldung, Dispoausgleich, Urlaubskredit, Autokredit, Möbel, Kredit ohne Bonitek...)</li>
      <li>- Kredite für Rentner bis 70 Jahre</li>
      <li>- Ratenkredit mit flexibler Laufzeit zwischen 12 und 120 Monate</li>
      <li>- Kredit ohne Bonitek möglich</li>
      <li>- Kostenloses Kreditangebot für Angestellte, Beamte, Rentner, Selbständige</li>
    </ul>
    <div class="card-divider"></div>
    <div class="cta-button"><span>Jetzt</span><span class="big">kostenlos</span><span>Kreditangebot</span><span>anfordern</span></div>
    <div class="guarantee">
      <h2>Garantie</h2>
      <p>Ihr Kreditangebot ist 100% kostenlos - zuverlässig seit mehr als 35 Jahren.</p>
    </div>
  </section>

  <svg class="abs starburst" viewBox="0 0 100 100" aria-hidden="true">
    <defs>
      <radialGradient id="burstFill" cx="45%" cy="40%" r="60%">
        <stop offset="0%" stop-color="#f2424a"/>
        <stop offset="100%" stop-color="#b8121c"/>
      </radialGradient>
    </defs>
    <polygon fill="url(#burstFill)" transform="rotate(-8 50 50)"
      points="100,50 90.2,58 96.2,69.2 84.1,72.8 85.4,85.4 72.8,84.1 69.2,96.2 58,90.2 50,100 42,90.2 30.8,96.2 27.2,84.1 14.6,85.4 15.9,72.8 3.8,69.2 9.8,58 0,50 9.8,42 3.8,30.8 15.9,27.2 14.6,14.6 27.2,15.9 30.8,3.8 42,9.8 50,0 58,9.8 69.2,3.8 72.8,15.9 85.4,14.6 84.1,27.2 96.2,30.8 90.2,42"/>
  </svg>
  <div class="abs starburst-text">Wir verhandelt<br>für Sie mit bis<br>zu 20 Banken -<br>kostenlos!</div>

  <div class="abs quality-badge" role="img" aria-label="Qualitätssiegel"></div>
  <div class="abs security-seal" role="img" aria-label="Siegel Datensicherheit"></div>

  <footer class="abs footer-bar"><span class="links">Impressum &nbsp;•&nbsp; Abmelden</span></footer>
</body>
</html>
```